freelance Nursing care

I'm starting my business as a freelance nurse. With this flyer, i would like to introduce my practice to the doctore as well as to the patients.<br/>my specialization is urodynamics and pelviperineology. i will be working as a consutant in my office and also in home care.<br/><br/>can you make a design with my logo and introduce my description in the flyer.

Target Market(s)

Doctor and patients

Industry/Entity Type

Health Care

Colors

Requirements
Must have
• - office and home cares services ( see in attache files). you can find it in Offre en soins en cabinet et à domicile
• - Advantage
• - training ( formation)
• -personal coordinate ( coordonnée personnelle)
• -Logo
Nice to have
• attractive design

```html
<!DOCTYPE html>
<html lang="fr">
<head>
<meta charset="utf-8">
<title>Infirmière Indépendante</title>
<link rel="stylesheet" href="https://fonts.googleapis.com/css2?family=Cabin:wght@400;600&family=Tinos:wght@700&family=Arimo:wght@700&display=swap">
<style>
:root{
  --navy:#1a4a92;
  --teal:#0aabc6;
  --teal-line:#1eb2c9;
  --heading-teal:#1a9fc0;
  --yellow:#fff23a;
  --ink:#1c1c1c;
  --light:#e4e7ea;
  --white:#ffffff;
}
*{margin:0;padding:0;box-sizing:border-box}
html,body{width:927px;height:1200px;overflow:hidden;background:var(--white)}
.flyer{position:relative;width:927px;height:1200px;overflow:hidden;font-family:"Cabin",sans-serif}
.backdrop{position:absolute;inset:0}
.title{position:absolute;left:0;width:964px;top:164px;text-align:center;font-family:"Tinos",serif;font-weight:700;font-size:52px;color:var(--yellow);letter-spacing:.5px}
.services{position:absolute;left:32px;top:374px;color:var(--white)}
.services h2{font-weight:600;font-size:27px;line-height:25px;color:var(--light);margin-bottom:25px}
.services li{font-size:20.5px;line-height:25.5px}
.side{position:absolute;left:483px;color:var(--ink)}
.advantages{top:374px}
.training{top:684px}
.side h2{font-weight:600;font-size:27px;line-height:32px;color:var(--heading-teal)}
.side li{font-size:19.3px;line-height:23.6px}
.side li.small{font-size:17.3px;line-height:21.5px}
ul{list-style:none}
li{position:relative;padding-left:27px;white-space:nowrap}
li::before{content:"";position:absolute;left:3px;top:.6em;width:9px;height:5px;border-bottom:1.5px solid var(--navy);border-radius:0 0 8px 8px;transform:rotate(-22deg)}
.services li::before{border-color:#2e5aa0}
.contact{position:absolute;left:0;width:920px;top:980px;text-align:center;font-family:"Arimo",sans-serif;font-weight:700;color:var(--white);font-size:23px;line-height:29.2px}
.contact h2{font-size:28px;line-height:32px;color:var(--yellow)}
</style>
</head>
<body>
<div class="flyer">
  <svg class="backdrop" width="927" height="1200" viewBox="0 0 927 1200" aria-hidden="true">
    <defs>
      <linearGradient id="divider" x1="0" x2="1">
        <stop offset="0" stop-color="#9a9a9a"/>
        <stop offset="1" stop-color="#ffffff" stop-opacity="0"/>
      </linearGradient>
      <linearGradient id="band" x1="0" x2="1">
        <stop offset="0" stop-color="#1eb2c9"/>
        <stop offset=".5" stop-color="#b7e4ec"/>
        <stop offset="1" stop-color="#1eb2c9"/>
      </linearGradient>
    </defs>
    <rect x="0" y="200" width="461" height="1000" fill="#0aabc6"/>
    <rect x="461" y="330" width="10" height="600" fill="url(#divider)"/>
    <path d="M0,0 H850 C930,40 935,170 880,240 C820,310 640,345 470,338 C300,330 120,285 0,232 Z" fill="#1a4a92" stroke="#1eb2c9" stroke-width="6"/>
    <path d="M461,918 C620,912 780,930 927,955 V1200 H461Z" fill="url(#band)"/>
    <path d="M40,1200 C50,1060 150,962 330,938 C550,916 750,936 927,970 V1200Z" fill="#1a4a92" stroke="#1eb2c9" stroke-width="5"/>
  </svg>

  <h1 class="title">Infirmiére Indépendante</h1>

  <section class="services">
    <h2>Offre en soins en<br>cabinet et à domicile</h2>
    <ul>
      <li>Enseignement en soins d’incontinence<br>(condoms, tampons, irrigation anale,<br>protection… etc.)</li>
      <li>Enseignement à l’auto-sondage</li>
      <li>Changement de sonde sus pubien ou<br>transurétrale</li>
      <li>Enseignement de neurostimulation<br>tibiale, intravaginale, vagale.</li>
      <li>Dilatations par hétéro-sondage</li>
      <li>Pansements etc</li>
      <li>Sous Mandat : Effectuer le bilan<br>urodynamique&nbsp; (BUD) en collaboration<br>avec médecin spécialiste.</li>
      <li>Pose de sonde nasogastrique, pose<br>VVP,&nbsp; PAC, perfusion des ATB etc…</li>
      <li>Contrôle de santé, préparation de<br>semainier</li>
    </ul>
  </section>

  <section class="side advantages">
    <h2>Avantages</h2>
    <ul>
      <li>Offrir un suivi personnalisé et de qualité à<br>chaque besoin, avec la même intervenante<br>ayant une expertise du domaine de<br>compétence.</li>
      <li>Promouvoir la plus grande autonomie et la<br>meilleure qualité de vie</li>
      <li>Conseils et promotion de la santé</li>
      <li>Intégrer le plus rapidement possible le<br>domicile après une hospitalisation</li>
      <li>Contribuer au développement de réseaux de<br>soin.</li>
    </ul>
  </section>

  <section class="side training">
    <h2>Formation</h2>
    <ul>
      <li>Participation aux divers congrès d’urologie<br>(SOFAP, IRUS, QAPE,<br>Symposium de Neuro urologie CHRL)</li>
      <li>Diplôme université d’urodynamique et<br>pelvi-périnéologie</li>
      <li class="small">Expériences divers (Oncologie, Gynécologie,<br>Urodynamique et pelvi-périnéologie)</li>
      <li class="small">Infirmière HES depuis 10 ans</li>
    </ul>
  </section>

  <section class="contact">
    <h2>Coordonnées personnelles</h2>
    <p>Consultation au cabinet</p>
    <p>Clinique des Rives</p>
    <p>Rue des Tilleuls 14</p>
    <p>2000 Valmont</p>
    <p>Tel : 076 000 12 34</p>
    <p>E-mail : contact.soins@exemple.ch</p>
  </section>
</div>
</body>
</html>
```